Personal Injury Law Firm needs folder design

Need a folder design for our personal injury law firm, Torrin & Mapley, LLC. to give to all of our clients with their documents at the end of their case. I've attached our branding guide. We are branded as the 5 star law firm that fights for our clients like family. It should incorporate our colors or Green and White. We'd like to convey a message of moving on to the next chapter after finishing their case.

```html
<!DOCTYPE html>
<html lang="en">
<head>
<meta charset="utf-8">
<title>Torrin &amp; Mapley, LLC. — Client Folder</title>
<link rel="stylesheet" href="https://fonts.googleapis.com/css2?family=Cinzel:wght@500&family=Montserrat:wght@400;600&family=Open+Sans:ital,wght@1,300&display=swap">
<style>
  :root {
    --brand-green: #17a67d;
    --white: #ffffff;
    --photo-light: #c9e59a;
    --photo-mid: #5ea94a;
    --photo-dark: #1f5a2e;
  }
  * { margin: 0; padding: 0; box-sizing: border-box; }
  html, body { width: 1200px; height: 776px; overflow: hidden; background: var(--brand-green); }
  .folder { position: relative; width: 1200px; height: 776px; }
  .panel { position: absolute; top: 0; width: 600px; height: 776px; background: var(--brand-green); color: var(--white); }
  .panel--back { left: 0; }
  .panel--front { left: 600px; }

  /* back panel */
  .promise {
    position: absolute; left: 0; width: 606px; top: 466px; text-align: center;
    font-family: "Montserrat", sans-serif; font-weight: 600; font-size: 18px;
    letter-spacing: 3px; color: var(--white); line-height: 1;
  }

  .firm-mark { position: absolute; display: flex; align-items: center; gap: 12px; }
  .firm-mark__square { width: 71px; height: 58px; background: var(--white); }
  .firm-mark__name { font-family: "Cinzel", serif; font-weight: 500; font-size: 19px; color: var(--white); white-space: nowrap; }
  .panel--back .firm-mark { left: 143px; top: 572px; }
  .panel--front .firm-mark { left: 242px; top: 666px; }

  .website {
    position: absolute; left: 143px; top: 672px; font-family: "Montserrat", sans-serif; font-weight: 400;
    font-size: 14px; letter-spacing: 4.5px; color: var(--white); white-space: nowrap;
  }

  /* front panel */
  .front-art { position: absolute; left: 0; top: 0; }
  .tagline {
    position: absolute; font-family: "Open Sans", sans-serif; font-style: italic; font-weight: 300;
    font-size: 42px; color: var(--white); white-space: nowrap; line-height: 1;
  }
  .tagline--one { left: 117px; top: 420px; }
  .tagline--two { left: 284px; top: 474px; }
</style>
</head>
<body>
<div class="folder">
  <section class="panel panel--back">
    <div class="promise">TRUSTED INJURY COUNSEL</div>

    <div class="firm-mark">
      <span class="firm-mark__square"></span>
      <span class="firm-mark__name">TORRIN &amp; MAPLEY, LLC.</span>
    </div>

    <div class="website">www.torrinandmapley.com</div>
  </section>

  <section class="panel panel--front">
    <svg class="front-art" width="600" height="776" viewBox="0 0 600 776">
      <defs>
        <linearGradient id="meadow" x1="0" y1="0" x2="0.4" y2="1">
          <stop offset="0" stop-color="var(--photo-mid)"/>
          <stop offset="0.35" stop-color="var(--photo-light)"/>
          <stop offset="0.6" stop-color="var(--photo-mid)"/>
          <stop offset="1" stop-color="var(--photo-dark)"/>
        </linearGradient>
      </defs>
      <rect width="600" height="776" fill="var(--brand-green)"/>
      <polygon role="img" aria-label="Photo: a family of four walking hand in hand through a sunlit flower meadow"
               points="0,0 600,0 600,195 63,776 0,776" fill="url(#meadow)"/>
    </svg>

    <div class="tagline tagline--one">Fighting for You</div>
    <div class="tagline tagline--two">Like Family</div>

    <div class="firm-mark">
      <span class="firm-mark__square"></span>
      <span class="firm-mark__name">TORRIN &amp; MAPLEY, LLC.</span>
    </div>
  </section>
</div>
</body>
</html>
```